Truck Driver Pay - Small Infographic

I need a very small, compact infographic to illustrate the differences in pay for a solo truck driver vs. team truck drivers. This illustration will be viewed on the web exclusively. I have sketched out an idea with all of the content that must be included. I just need a designer's touch.

The attached 'mock up' contains the information to be illustrated/communicated by this infographic.

Target Market(s)

Blue collar employee males ages 18-49 with high school education

Requirements
Must have
• I need 2 versions of the graphic:
• 1) 600 pixels wide for desktop presentation
• 2) 300 pixels wide with vertical scroll for mobile.
• I also require the native .psd or .ai files used to create this infographic.

```html
<!DOCTYPE html>
<html lang="en">
<head>
<meta charset="utf-8">
<title>Understanding Driver Pay</title>
<link rel="stylesheet" href="https://fonts.googleapis.com/css2?family=Titan+One&family=Roboto:wght@500;700&family=Tinos:ital,wght@0,400;0,700;1,700&display=swap">
<style>
  :root {
    --sky-top: #9fd3f2;
    --sky-bottom: #e4f3fb;
    --title-yellow: #ffd23c;
    --title-stroke: #8b1d2c;
    --banner-orange: #f58a2a;
    --banner-orange-dark: #e0701a;
    --maroon: #7d1e2a;
    --driver-blue: #1c6fa8;
    --ink: #1d2a44;
    --divider: #ffffff;
    --sun: #ffe46b;
  }
  * { margin: 0; padding: 0; box-sizing: border-box; }
  html, body { width: 920px; height: 1200px; overflow: hidden; }
  body {
    position: relative;
    background: linear-gradient(180deg, var(--sky-top) 0%, var(--sky-bottom) 45%, #f2f9fd 100%);
    font-family: "Tinos", "Times New Roman", serif;
    color: var(--ink);
  }
  .sky-decor {
    position: absolute; left: 560px; top: 0; width: 300px; height: 150px;
    background: radial-gradient(circle at 60% 25%, var(--sun) 0 40px, rgba(255,228,107,0.35) 60px, rgba(255,255,255,0) 120px);
  }
  h1 { font-weight: normal; }
  .title-word {
    position: absolute;
    font-family: "Titan One", "Arial Black", sans-serif;
    color: var(--title-yellow);
    -webkit-text-stroke: 3px var(--title-stroke);
    paint-order: stroke fill;
    text-shadow: 0 4px 0 var(--title-stroke);
    line-height: 1;
    letter-spacing: 1px;
    white-space: nowrap;
  }
  .title-understanding { left: 38px; top: 36px; font-size: 62px; transform: rotate(-3deg); transform-origin: left top; }
  .title-pay { left: 690px; top: 52px; font-size: 58px; transform: rotate(8deg); }
  .title-driver { left: 436px; top: 108px; font-size: 56px; transform: rotate(-2deg); }

  .divider { position: absolute; left: 459px; top: 190px; width: 3px; height: 990px; background: var(--divider); }

  .banner {
    position: absolute;
    height: 76px;
    background: var(--banner-orange);
    clip-path: polygon(0 8%, 100% 0, 97% 50%, 100% 100%, 0 92%, 2% 50%);
    color: #fff;
    font-family: "Roboto", Arial, sans-serif;
    font-weight: 500;
    font-size: 42px;
    display: flex; align-items: center; justify-content: center;
    box-shadow: inset 0 -6px 0 var(--banner-orange-dark);
  }
  .banner-solo { left: 28px; top: 216px; width: 350px; }
  .banner-team { left: 483px; top: 216px; width: 420px; }
  .banner-check { top: 620px; height: 62px; font-size: 36px; }
  .banner-check.left { left: 28px; width: 415px; }
  .banner-check.right { left: 483px; width: 420px; }

  .figure { position: absolute; border-radius: 10px; }
  .truck { background: linear-gradient(180deg, #8e2a36, var(--maroon)); }
  .person { background: linear-gradient(180deg, #2a84bf, var(--driver-blue)); border-radius: 22px; }
  .truck-solo { left: 55px; top: 310px; width: 140px; height: 200px; }
  .person-solo { left: 295px; top: 368px; width: 48px; height: 122px; }
  .truck-team { left: 507px; top: 310px; width: 140px; height: 200px; }
  .person-team { left: 738px; top: 368px; width: 150px; height: 122px; }

  .count {
    position: absolute; top: 544px;
    font-family: "Roboto", Arial, sans-serif; font-weight: 700; font-size: 40px;
    line-height: 1;
  }
  .count.truck-label { color: var(--maroon); }
  .count.driver-label { color: var(--driver-blue); }

  .calc { position: absolute; top: 700px; text-align: center; font-size: 24px; line-height: 1; }
  .calc .row { height: 42px; }
  .calc .rule { height: 2px; background: var(--ink); margin: -6px 0 12px; }
  .calc .times { position: absolute; left: -4px; top: 30px; font-size: 20px; }
  .calc-solo { left: 40px; width: 330px; }
  .calc-team { left: 495px; width: 320px; }

  .badge {
    position: absolute; width: 80px; height: 62px; border-radius: 50%;
    background: var(--maroon); color: #fff;
    font-style: italic; font-weight: 700; font-size: 16px; line-height: 1.05;
    display: flex; align-items: center; justify-content: center; text-align: center;
  }
  .badge-solo { left: 378px; top: 740px; }
  .badge-team { left: 812px; top: 786px; }
  .pointer { position: absolute; overflow: visible; }

  .note { position: absolute; width: 420px; font-size: 22px; line-height: 1.2; color: var(--ink); white-space: nowrap; }
  .note p + p { margin-top: 24px; }
  .note-solo { left: 36px; top: 896px; }
  .note-team { left: 490px; top: 896px; }
</style>
</head>
<body>
  <div class="sky-decor" role="img" aria-label="Sun and light clouds in the sky"></div>

  <h1>
    <span class="title-word title-understanding">UNDERSTANDING</span>
    <span class="title-word title-pay">PAY</span>
    <span class="title-word title-driver">DRIVER</span>
  </h1>

  <div class="divider"></div>

  <section class="column-solo">
    <h2 class="banner banner-solo">Solo Driver Pay</h2>
    <div class="figure truck truck-solo" role="img" aria-label="Front view of a semi truck"></div>
    <div class="figure person person-solo" role="img" aria-label="One driver figure"></div>
    <div class="count truck-label" style="left:55px">1 Truck</div>
    <div class="count driver-label" style="left:242px">1 Driver</div>

    <h3 class="banner banner-check left">Example Pay Check</h3>
    <div class="calc calc-solo">
      <span class="times">x</span>
      <div class="row">2500 Weekly Miles Driven*</div>
      <div class="row">.26 Mileage Rate</div>
      <div class="rule"></div>
      <div class="row">$650 Weekly Pay</div>
    </div>
    <svg class="pointer" style="left:318px;top:756px" width="60" height="26" viewBox="0 0 60 26">
      <path d="M2 22 Q34 24 54 8" fill="none" stroke="#1c6fa8" stroke-width="3"/>
      <path d="M46 5 L58 4 L55 15 Z" fill="#1c6fa8"/>
    </svg>
    <div class="badge badge-solo">Classic<br>Plan</div>

    <div class="note note-solo">
      <p>When a solo driver needs to take his<br>required break, the truck has to stop<br>rolling.</p>
      <p>Solo drivers can drive a limited<br>amount of miles due to mandated<br>breaks and rest safety regulations.</p>
    </div>
  </section>

  <section class="column-team">
    <h2 class="banner banner-team">Team Driver Pay</h2>
    <div class="figure truck truck-team" role="img" aria-label="Front view of a semi truck"></div>
    <div class="figure person person-team" role="img" aria-label="Two driver figures"></div>
    <div class="count truck-label" style="left:507px">1 Truck</div>
    <div class="count driver-label" style="left:710px">2 Drivers</div>

    <h3 class="banner banner-check right">Example Pay Check</h3>
    <div class="calc calc-team">
      <span class="times">x</span>
      <div class="row">4200 Weekly Miles Driven*</div>
      <div class="row">.175 Mileage Rate</div>
      <div class="rule"></div>
      <div class="row">$752 Weekly Pay</div>
    </div>
    <svg class="pointer" style="left:752px;top:800px" width="62" height="24" viewBox="0 0 62 24">
      <path d="M2 18 Q32 20 54 10" fill="none" stroke="#1c6fa8" stroke-width="3"/>
      <path d="M48 4 L60 9 L51 18 Z" fill="#1c6fa8"/>
    </svg>
    <div class="badge badge-team">Each<br>Driver</div>

    <div class="note note-team">
      <p>Team drivers alternate driving duties<br>so the truck cover more miles.<br>When Driver 1 needs to take his<br>required break,Driver 2 takes over<br>driving duties until his required break<br>and they switch places again.</p>
      <p>The truck keeps rolling and both<br>drivers are paid for combined miles<br>the truck has been driven.</p>
    </div>
  </section>
</body>
</html>
```